LumaDerm business cards

We want to create two sets of cards. One general card for lumaderm [staff] and one card for the founder of the company. Below is the general/basic information for you to format/display on side of the cards:
--Company address: 418 Harlow Street, New York, NY 10027
--Main phone: 212-637-1582
Will also provide you with secondary 1-800 number
--company website: www.lumaderm-example.com
--email address for general card: concierge@lumaderm-example.com
--email address (for dr whitfield's card: dr@lumaderm-example.com
--titles for dr whitfield's card: Founder, Medical Director
--Dr. Whitfield's name on the card should read: Gregory T. Whitfield, MD
You can also play around with lumaderm's tag line: Radiance Kept Quietly Yours (TM or R should be attached as a trademark has been filed)
Reason: More time to design something awesome. This company is an aesthetic medical company that offers cool and safe cosmetic treatments
For the business card design for the doctor, please change the doctor's name to look like this above his title: Gregory T. Whitfield, MD instead of using Dr. Gregory....etc
Reason: WILL NOT BE ABLE TO VIEW AND FINALIZE DESIGNS UNTIL I RETURN FROM MEDICAL CONFERENCE, WHICH WILL BE ON SUNDAY/MONDAY. MY APOLOGIES
can everyone try making it very minimalistic
A Bit of a change...
Can everyone take a stab at using a grey "raw" or eco friendly stock paper. We are interested to see the designs you come up with.
Business

```html
<!DOCTYPE html>
<html lang="en">
<head>
<meta charset="utf-8">
<title>LumaDerm business cards</title>
<link rel="stylesheet" href="https://fonts.googleapis.com/css2?family=Arimo:wght@400;700&display=swap">
<style>
  :root {
    --stage: #e4e5e7;
    --stage-light: #f4f4f5;
    --stock-grey: #e6e5e1;
    --stock-grey-deep: #dcdbd6;
    --brand-blue: #3a9fd8;
    --on-blue: #ffffff;
    --ink: #2e2e2e;
    --rule: #bdbcb7;
    --band-dark: #3b3b3d;
  }
  * { margin: 0; padding: 0; box-sizing: border-box; }
  html, body { width: 1038px; height: 1200px; overflow: hidden; }
  body {
    background: radial-gradient(ellipse at 50% 40%, var(--stage-light), var(--stage));
    font-family: "Arimo", Arial, sans-serif;
    color: var(--ink);
    position: relative;
  }
  .card {
    position: absolute;
    left: 99px;
    width: 840px;
    height: 482px;
    box-shadow: 0 6px 14px rgba(0,0,0,0.22);
    overflow: hidden;
  }
  .card-front {
    top: 80px;
    background: linear-gradient(135deg, var(--stock-grey), var(--stock-grey-deep));
  }
  .card-back { top: 640px; background: var(--brand-blue); }

  .wordmark {
    position: absolute;
    font-weight: 400;
    font-size: 68px;
    letter-spacing: -1px;
    line-height: 1;
  }
  .tagline {
    position: absolute;
    font-size: 10px;
    letter-spacing: 1.6px;
    text-transform: uppercase;
    line-height: 1;
  }
  .card-front .wordmark { right: 78px; top: 88px; color: var(--brand-blue); }
  .card-front .tagline { right: 132px; top: 164px; color: var(--brand-blue); }

  .holder-name {
    position: absolute; left: 66px; top: 232px;
    font-size: 23px; font-weight: 700; color: var(--brand-blue);
  }
  .holder-title {
    position: absolute; left: 66px; top: 266px;
    font-size: 19px; color: var(--ink);
  }
  .divider {
    position: absolute; left: 318px; right: 56px; top: 276px;
    height: 1px; background: var(--rule);
  }
  .address {
    position: absolute; left: 66px; top: 354px;
    font-size: 18px; line-height: 29px; font-style: normal;
  }
  .contact-list {
    position: absolute; right: 50px; top: 298px;
    list-style: none; text-align: right;
    font-size: 18px; line-height: 28.5px;
  }
  .contact-list li { display: flex; justify-content: flex-end; align-items: center; gap: 14px; }
  .contact-list svg { width: 15px; height: 15px; flex: none; }

  .footer-band { position: absolute; left: 0; bottom: 0; width: 840px; height: 30px; }

  .card-back .wordmark { left: 0; right: 0; top: 196px; text-align: center; color: var(--on-blue); font-size: 72px; }
  .card-back .tagline { left: 0; right: 0; top: 278px; text-align: center; color: var(--on-blue); opacity: 0.9; }
</style>
</head>
<body>

<section class="card card-front" aria-label="Business card, front">
  <div class="wordmark">lumaderm</div>
  <div class="tagline">Radiance Kept Quietly Yours™</div>

  <div class="holder-name">Gregory T. Whitfield, MD</div>
  <div class="holder-title">Founder, Medical Director</div>
  <div class="divider"></div>

  <address class="address">418 Harlow Street<br>New York, NY 10027</address>

  <ul class="contact-list">
    <li>212-637-1582
      <svg viewBox="0 0 16 16"><path fill="var(--brand-blue)" d="M3.6 1.5l2.3 2.6-1.2 1.8c.9 2 2.4 3.6 4.4 4.6l1.8-1.2 2.6 2.3-1.4 2.4C7.3 13.6 2.4 8.7 1.2 2.9z"/></svg></li>
    <li>(1-800) 212-637-1582
      <svg viewBox="0 0 16 16"><path fill="var(--brand-blue)" d="M3.6 1.5l2.3 2.6-1.2 1.8c.9 2 2.4 3.6 4.4 4.6l1.8-1.2 2.6 2.3-1.4 2.4C7.3 13.6 2.4 8.7 1.2 2.9z"/></svg></li>
    <li>concierge@lumaderm-example.com
      <svg viewBox="0 0 16 16"><rect x="1" y="3.5" width="14" height="9.5" rx="1" fill="var(--brand-blue)"/><path d="M1.5 4l6.5 5 6.5-5" fill="none" stroke="#fff" stroke-width="1.2"/></svg></li>
    <li>dr@lumaderm-example.com
      <svg viewBox="0 0 16 16"><rect x="1" y="3.5" width="14" height="9.5" rx="1" fill="var(--brand-blue)"/><path d="M1.5 4l6.5 5 6.5-5" fill="none" stroke="#fff" stroke-width="1.2"/></svg></li>
    <li>www.lumaderm-example.com
      <svg viewBox="0 0 16 16"><circle cx="8" cy="8" r="7" fill="var(--brand-blue)"/><g fill="none" stroke="#fff" stroke-width="1"><ellipse cx="8" cy="8" rx="3" ry="6.5"/><path d="M1.5 8h13M2.5 4.8h11M2.5 11.2h11"/></g></svg></li>
  </ul>

  <svg class="footer-band" viewBox="0 0 840 30" preserveAspectRatio="none">
    <rect width="840" height="30" fill="var(--band-dark)"/>
    <polygon points="0,0 510,0 486,30 0,30" fill="var(--brand-blue)"/>
  </svg>
</section>

<section class="card card-back" aria-label="Business card, back">
  <div class="wordmark">lumaderm</div>
  <div class="tagline">Radiance Kept Quietly Yours™</div>
</section>

</body>
</html>
```